Fontenot Bayou Grillhouse (Owners Card)

Need a classy, but modern business card. I have included a promotional card for the steakhouse. I need one for myself (the owner) that is more professional.

Target Market(s)

General Public

Industry/Entity Type

Food service

Contact Information for Business Card

Name, business address, phone number, email, logo

Font styles to use
Serif
Sans Serif
Decorative
Script

Requirements
Must have
• My name (Darvel Pruitt), business address (327 Oakmere Street), phone number (510) 493-2615, email (Dpruittkr4@mailvane.example. On the back of the card: Psalms 27 1 The LORD is my light and my salvation— whom shall I fear? The LORD is the stronghold of my life— of whom shall I be afraid? 2 When the wicked advance against me to devour me, it is my enemies and my foes who will stumble and fall. 3 Though an army besiege me, my heart will not fear; though war break out against me, even then I will be confident.
Nice to have
• Something that’s bold, but modern and professional.

```html
<!DOCTYPE html>
<html lang="en">
<head>
<meta charset="utf-8">
<title>Fontenot Bayou Grillhouse – Owner Business Card</title>
<link rel="stylesheet" href="https://fonts.googleapis.com/css2?family=Open+Sans:wght@400;600;700;800&display=swap">
<style>
  :root {
    --stage: #232323;
    --card: #141414;
    --card-edge: #0b0b0b;
    --green: #14a84a;
    --yellow: #f7d416;
    --orange: #f7941d;
    --red: #ec2227;
    --text: #f2f2f2;
    --muted: #d9d9d9;
    --rasta: linear-gradient(90deg, var(--green) 0%, var(--green) 28%, var(--yellow) 50%, var(--orange) 60%, var(--red) 72%, var(--red) 100%);
  }
  * { box-sizing: border-box; margin: 0; padding: 0; }
  html, body {
    width: 1200px; height: 780px; overflow: hidden;
    background: var(--stage);
    font-family: "Open Sans", Arial, sans-serif;
    color: var(--text);
  }
  .canvas {
    position: relative; width: 1200px; height: 780px;
    display: flex; align-items: center; justify-content: center; gap: 40px;
  }
  .card {
    position: relative; width: 560px; height: 320px;
    background: var(--card); border-radius: 18px; overflow: hidden;
    box-shadow: 0 14px 30px rgba(0,0,0,.55), 0 0 0 1px var(--card-edge);
  }

  /* ---------- brand name block ---------- */
  .brand { display: flex; align-items: center; gap: 10px; }
  .brand__dot {
    width: 16px; height: 16px; border-radius: 50%;
    background: var(--orange); flex: none;
  }
  .brand__name {
    font-weight: 800; color: var(--orange);
    text-transform: uppercase; letter-spacing: .04em; line-height: 1.1;
  }

  /* ---------- back: scripture side ---------- */
  .scripture .ornament {
    position: absolute; left: 70px; top: 10px; width: 420px; height: 260px;
    border-radius: 50%;
    background: radial-gradient(ellipse at center, rgba(60,60,60,.35) 0%, rgba(20,20,20,0) 70%);
  }
  .scripture .brand { position: absolute; top: 58px; left: 0; right: 0; justify-content: center; }
  .scripture .brand__name { font-size: 22px; }
  .verse-rule {
    position: absolute; top: 150px; left: 24px; right: 24px; height: 20px;
    display: flex; align-items: center; gap: 10px;
  }
  .verse-rule__line { flex: 1; height: 2px; }
  .verse-rule__line--left { background: linear-gradient(90deg, transparent, var(--red) 30%, var(--yellow) 65%, var(--green)); }
  .verse-rule__line--right { background: linear-gradient(90deg, var(--green), var(--yellow) 35%, var(--red) 70%, transparent); }
  .verse-badge {
    padding: 3px 14px; border-radius: 12px;
    background: linear-gradient(180deg, var(--red) 0%, var(--red) 60%, var(--green) 100%);
    font-weight: 700; font-size: 13px; letter-spacing: .02em; color: #fff;
  }
  .verses {
    position: absolute; top: 188px; left: 20px; right: 20px;
    display: grid; grid-template-columns: repeat(3, 1fr); gap: 16px;
  }
  .verse {
    font-size: 11px; line-height: 1.45; text-align: center; color: var(--muted);
  }

  /* ---------- front: owner side ---------- */
  .owner .brand { position: absolute; left: 40px; top: 120px; width: 250px; }
  .owner .brand__name { font-size: 21px; }
  .owner .divider {
    position: absolute; left: 318px; top: 50px; width: 2px; height: 160px;
    background: linear-gradient(180deg, var(--red), var(--yellow) 55%, var(--green));
  }
  .person { position: absolute; left: 345px; top: 70px; }
  .person__name { font-size: 26px; font-weight: 800; line-height: 1.1; }
  .person__first { color: var(--green); }
  .person__last { color: var(--red); }
  .person__role { font-size: 13px; font-weight: 600; margin-top: 2px; }
  .contacts { list-style: none; margin-top: 16px; }
  .contacts li {
    display: flex; align-items: center; gap: 7px;
    font-size: 12px; line-height: 1.75;
  }
  .contacts svg { width: 12px; height: 12px; flex: none; }
  .address-band {
    position: absolute; left: 0; right: 0; bottom: 30px; height: 26px;
    background: var(--rasta);
    display: flex; align-items: center; padding-left: 280px;
    font-size: 13px; font-weight: 600; color: #fff;
  }
  .band-mark {
    position: absolute; right: 22px; bottom: 32px; width: 22px; height: 22px;
    border-radius: 50%; background: var(--orange);
  }
</style>
</head>
<body>
<main class="canvas">

  <section class="card scripture" aria-label="Card back with Psalm 27">
    <div class="ornament" role="img" aria-label="Faint decorative carnival flourish in the background"></div>
    <div class="brand">
      <span class="brand__dot"></span>
      <span class="brand__name">Fontenot Bayou Grillhouse</span>
    </div>
    <div class="verse-rule">
      <span class="verse-rule__line verse-rule__line--left"></span>
      <span class="verse-badge">PSALMS 27</span>
      <span class="verse-rule__line verse-rule__line--right"></span>
    </div>
    <div class="verses">
      <p class="verse">The LORD is my light and my salvation—whom shall I fear? The LORD is the stronghold of my life—of whom shall I be afraid?</p>
      <p class="verse">Though an army besiege me, my heart will not fear; though war break out against me, even then I will be confident.</p>
      <p class="verse">When the wicked advance against me to devour me, it is my enemies and my foes who will stumble and fall.</p>
    </div>
  </section>

  <section class="card owner" aria-label="Card front with owner details">
    <div class="brand">
      <span class="brand__dot"></span>
      <span class="brand__name">Fontenot Bayou Grillhouse</span>
    </div>
    <span class="divider"></span>
    <div class="person">
      <h1 class="person__name"><span class="person__first">Darvel</span> <span class="person__last">Pruitt</span></h1>
      <p class="person__role">Owner</p>
      <ul class="contacts">
        <li>
          <svg viewBox="0 0 24 24" aria-hidden="true"><path fill="#ec2227" d="M6.6 10.8a15.1 15.1 0 0 0 6.6 6.6l2.2-2.2a1 1 0 0 1 1-.25 11.4 11.4 0 0 0 3.6.57 1 1 0 0 1 1 1V20a1 1 0 0 1-1 1A17 17 0 0 1 3 4a1 1 0 0 1 1-1h3.5a1 1 0 0 1 1 1c0 1.25.2 2.45.57 3.57a1 1 0 0 1-.25 1z"/></svg>
          (510) 493-2615
        </li>
        <li>
          <svg viewBox="0 0 24 24" aria-hidden="true"><circle cx="12" cy="12" r="10" fill="none" stroke="#f7d416" stroke-width="2.4"/><path d="M2 12h20M12 2c3 3 3 17 0 20M12 2c-3 3-3 17 0 20" fill="none" stroke="#14a84a" stroke-width="1.8"/></svg>
          www.fontenotbayou.example
        </li>
        <li>
          <svg viewBox="0 0 24 24" aria-hidden="true"><rect x="2" y="5" width="20" height="14" rx="2" fill="#14a84a"/><path d="M3 6l9 7 9-7" fill="none" stroke="#ec2227" stroke-width="2"/></svg>
          Dpruittkr4@mailvane.example
        </li>
      </ul>
    </div>
    <div class="address-band">327 Oakmere Street</div>
    <span class="band-mark"></span>
  </section>

</main>
</body>
</html>
```